Puerto Rican fusion Bistro RESTAURANT FAMILY owned

Tomas's Bistro offers to you and your guests, a unique culinary Caribbean experience, steeped in Puerto Rican hospitality, while keeping local sustainability in mind. Located in the heart of "Cedar Hollow" we understand that the locally owned small business is the heart of our economy. We are investing in our communities future by seeking out and partnering with quality local suppliers and growers, from our meats to produce and wines to provide the best dinning experience possible. We are proud to invest in Lorvania, and are proud of these partnerships strengthening our commitment. From start to finish, Chef Tomas Arroyo & the Team of Tomas's Bistro will partner with you to create a memorable gathering for you and your entire party. Creativity and flare is the hallmark of event catered by Tomas's Bistro. Menu planning, decor, and service options are carefully orchestrated so your affair goes off without a hitch. Whether you choose our private dining room, our intimate patio setting or an off site location of your choosing we handle all of the details at your direction
As the only chef in Cedar Hollow and one of the few on the south side, owner and Chef Tomas Arroyo presents a fresh approach offering a growing trend in an open kitchen in order to be close to our guests. If its a last minute healthy lunch for fifteen, a hot, healthy, trendy dinner for 50, or appetizers for 500 of your closest friends, the team at Tomas's Bistro can accommodate all of your needs. Calling on a vast reservoir of personal recipes and experiences creating gourmet dishes, featuring wild game, Ahi Tuna, lamb and seafood is the canvas on which the chef creates. Food includes wines and craft beers pairings. We can accommodate a variety of special dietary needs.
TOMAS SR. ARROYO
BIO
SOUTH BEND, INDIANA 46614
Current owner and Chef of Tomas’s Bistro, 2years open and still going strong. Back ground family of 12 brothers and sisters from one parent. 3rd from the last bunch

WORK HISTORY

Dunleavy’s at the Quayside 2 ½ years Chef and Food & Beverage Director. Greystone Medical Center, South Bend 6 ½ years, Sous Chef to Chef/Manager, Reorganization of kitchen for efficiency of production. Operational Effectiveness Initiated aggressive Patient meal service, Halvorn Ratings scores of 80.7% from 70%, by reimaging the patient meals and tray presentation with an upscale quality service, changed the menu from a seven day cycle to a restaurant style menu to include total production process and implementing higher standards, introduced new technology for quality culinary production.
Bellweather Restaurant, Chef/Manager, Carbone’s Italian Restorante, Chef/Manager, October 22, 2001 article in the Fairmont Courier “PAST the Plate”, Copper Prairie Steak House, San Antonio TX, Increased revenue $2000 a day by implementing lunch dining and catering business which did not exist at the time. Cooked meals for 700 guest for dinner which consisted of seafood and steaks on a mesquite grill

EDUCATION/PROFESSIONAL DEVELOPMENT
Thornfield Culinary of Arts School, Chicago, Il

Thank You for considering Tomas's Bistro to partner with you for your next event

Target Market(s)

20-65

Industry/Entity Type

Restaurant

Font styles to use
Serif

Colors

Designer to choose colors to be used in the design.

Requirements
Must have
• descriptions, include kids menu pictures and mimosas including noting we have only craft beers and great wine selection
Nice to have
• breakfast on one page lunch on second page dinner on 4th page pizza on fith pager

```html
<!DOCTYPE html>
<html lang="en">
<head>
<meta charset="utf-8">
<title>Tomas's Bistro — Dinner Menu</title>
<link href="https://fonts.googleapis.com/css2?family=Bodoni+Moda:ital,wght@0,400;1,400&family=Jost:wght@300;400;500;600&display=swap" rel="stylesheet">
<style>
  :root {
    --sun: #fdb913;
    --paper: #ffffff;
    --ink: #1f1f1f;
    --ink-soft: #3a3a3a;
    --photo-dark: #3b3b3b;
    --photo-light: #d9d9d9;
    --ring: #e7cfb4;
  }
  * { box-sizing: border-box; margin: 0; padding: 0; }
  html, body { width: 849px; height: 1200px; overflow: hidden; }
  body { background: var(--sun); font-family: "Jost", sans-serif; color: var(--ink); }
  .menu { position: relative; width: 849px; height: 1200px; }
  .sheet { position: absolute; left: 42px; top: 42px; width: 764px; height: 1116px; background: var(--paper); }

  .intro {
    position: absolute; left: 66px; top: 72px; width: 562px;
    font-family: "Bodoni Moda", serif; font-size: 14.6px; line-height: 14px;
    letter-spacing: 0.5px; text-transform: uppercase; color: var(--ink);
  }
  .intro-rule { position: absolute; left: 70px; top: 199px; width: 564px; height: 1px; background: var(--sun); }
  .chef-portrait {
    position: absolute; left: 634px; top: 56px; width: 172px; height: 146px;
    border-radius: 50%; border: 2px solid var(--ring);
    background: radial-gradient(ellipse at 50% 50%, #6e6e6e 0%, #a9a9a9 38%, #ffffff 62%);
  }

  .section-title {
    position: absolute; color: var(--sun); font-weight: 500; font-size: 21px;
    letter-spacing: 4.2px; text-align: center; text-transform: uppercase;
  }
  .section-title small { display: block; font-size: 10px; letter-spacing: 3px; line-height: 10px; }
  .section-rule { position: absolute; height: 1.5px; background: var(--sun); }

  .column { position: absolute; width: 222px; }
  .item { margin-bottom: 8px; }
  .item-head { display: grid; grid-template-columns: 1fr 30px; align-items: baseline; }
  .item-name { font-weight: 600; font-size: 11.2px; letter-spacing: 0.3px; text-transform: uppercase; }
  .price { font-family: "Bodoni Moda", serif; font-size: 10px; }
  .desc { font-weight: 300; font-size: 8.6px; line-height: 10.2px; letter-spacing: 0.2px; text-transform: uppercase; color: var(--ink-soft); }
  .col-appetizers .desc { width: 194px; }
  .col-burger .desc { width: 172px; }
  .col-entree .desc { width: 196px; }
  .col-wide .desc { width: 198px; }
  .desc .note { font-size: 7.4px; }
  .subline { display: grid; grid-template-columns: 1fr 30px; font-weight: 300; font-size: 8.8px; line-height: 12px; text-transform: uppercase; }
  .subline .price { font-size: 10px; }
  .lead { width: 222px; text-align: center; font-weight: 300; font-size: 9.4px; line-height: 10.4px; text-transform: uppercase; margin-bottom: 12px; }
  .script { font-family: "Bodoni Moda", serif; font-style: italic; font-size: 9.6px; text-transform: uppercase; color: var(--sun); letter-spacing: 0.3px; }
  .script-dark { font-family: "Bodoni Moda", serif; font-style: italic; font-size: 8px; text-transform: uppercase; line-height: 9px; color: var(--ink-soft); }
  .addon { font-family: "Bodoni Moda", serif; font-size: 8px; text-align: right; padding-right: 18px; text-transform: uppercase; }
  .addon .price { margin-left: 8px; }

  .chef-feature {
    position: absolute; left: 560px; top: 708px; width: 246px; height: 450px;
    background: linear-gradient(180deg, #d8d8d8 0%, #8f8f8f 24%, var(--photo-dark) 65%, #2a2a2a 100%);
    border-radius: 46% 46% 0 0 / 22% 22% 0 0;
  }
  .hours-card {
    position: absolute; left: 640px; top: 1014px; width: 98px; height: 122px;
    background: var(--paper); border: 2px solid var(--ink);
    text-align: center; padding-top: 8px; text-transform: uppercase;
  }
  .hours-card .big { font-weight: 600; font-size: 19px; line-height: 19px; }
  .hours-card .bigger { font-weight: 600; font-size: 24px; line-height: 22px; }
  .hours-card .time { font-weight: 600; font-size: 15px; margin-top: 6px; line-height: 15px; }
  .hours-card .small { font-weight: 400; font-size: 12px; letter-spacing: 1.5px; line-height: 14px; }

  .fine-print { position: absolute; left: 70px; top: 1062px; width: 220px; }
  .fine-print .desc { font-size: 8.2px; line-height: 10px; }
</style>
</head>
<body>
<main class="menu">
  <div class="sheet"></div>

  <p class="intro">Tomas's Bistro offers a taste of Puerto Rico, a Caribbean culture, famously known as “El Borinqueno”. There are two basic components, which makes our flavors unique and robust. Sofrito is our number one ingredient, made up of fresh home grown vegetables. Adobo is the main seasoning we use. All our culinary creations use's these two ingredients offering you an authentic taste only found in the “El Borinqueno” culture.</p>
  <div class="intro-rule"></div>
  <div class="chef-portrait" role="img" aria-label="Photo of the chef in a black chef coat holding two plated dishes, framed by a coffee ring"></div>

  <!-- Appetizers -->
  <h2 class="section-title" style="left:68px;top:208px;width:228px;">Appetizers<small>(Frituras)</small></h2>
  <div class="section-rule" style="left:70px;top:254px;width:224px;"></div>
  <section class="column col-appetizers" style="left:68px;top:269px;">
    <div class="item"><div class="item-head"><span class="item-name">Grilled or Fried Calamari</span><span class="price">10</span></div>
      <p class="desc">Grilled is served with ginger dressing &amp; TB's dipping sauce. Fried is served with TB's sauce</p></div>
    <div class="item"><div class="item-head"><span class="item-name">Latino Fondue</span><span class="price">7</span></div>
      <p class="desc">Smoked cheddar blend, peppers, onions, sofrito served with house-made tortilla chips</p></div>
    <div class="item"><div class="item-head"><span class="item-name">Fried Pickles</span><span class="price">7</span></div>
      <p class="desc">Lightly breaded and served<br>with TB's sauce</p></div>
    <div class="item"><div class="item-head"><span class="item-name">Nachos</span><span class="price">9</span></div>
      <p class="desc">Bistro potato's with picadillo, Latino cheese sauce, jalapenos, green onion, house-made guacamole and pico with sour cream</p></div>
    <div class="item"><div class="item-head"><span class="item-name">Mojito Carne Frita</span><span class="price">7</span></div>
      <p class="desc">Citrus marinated pork fried chunks, topped with fried onions and tortilla</p></div>
    <div class="item"><div class="item-head"><span class="item-name">Nachos</span><span class="price">9</span></div>
      <p class="desc">Bistro potato's with picadillo, Latino cheese sauce, jalapenos, green onion, house-made guacamole and pico with sour cream</p></div>
    <div class="item"><div class="item-head"><span class="item-name">Quesadilla</span><span></span></div>
      <div class="subline"><span>Cheese</span><span class="price">8</span></div>
      <div class="subline"><span>Veggie or chicken</span><span class="price">11</span></div>
      <div class="subline"><span>Pork mojito, steak or picadillo</span><span class="price">14</span></div>
      <div class="subline"><span>Salmon or shrimp</span><span class="price">16</span></div></div>
    <div class="item" style="margin-top:12px;margin-bottom:12px;"><div class="item-head"><span class="item-name">Fried Onion Rings</span><span class="price">7/15</span></div></div>
    <div class="item"><div class="item-head"><span class="item-name">Assorted Chips-n-Salsa</span><span class="price">7</span></div></div>
  </section>

  <!-- Burger -->
  <h2 class="section-title" style="left:312px;top:220px;width:224px;">Burger</h2>
  <div class="section-rule" style="left:312px;top:254px;width:224px;"></div>
  <section class="column col-burger" style="left:311px;top:269px;">
    <p class="lead">Accompanied with bistro potatoes, topped with TB's sauce, lettuce, tomato pickle and red onion</p>
    <div class="item"><div class="item-head"><span class="item-name">Beefy Beef Burger</span><span class="price">12</span></div>
      <p class="desc">Flank steak, grilled onions and mozzarella</p></div>
    <div class="item"><div class="item-head"><span class="item-name">Latino Burger</span><span class="price">9</span></div>
      <p class="desc">Pico, guacamole, cheddar and provolone cheeses</p></div>
    <div class="item"><div class="item-head"><span class="item-name">Barnyard Burger</span><span class="price">10</span></div>
      <p class="desc">Beef, bacon and egg</p></div>
    <div class="item"><div class="item-head"><span class="item-name">Mojito Burger</span><span class="price">10</span></div>
      <p class="desc">Bacon and pork mojito, onion and provolone</p></div>
    <div class="item"><div class="item-head"><span class="item-name">Bleu Mushroom Burger</span><span class="price">10</span></div>
      <p class="desc">Bleu cheese, sautéed mushroom, grilled onion and black pepper</p></div>
    <div class="item"><div class="item-head"><span class="item-name">Veggie Burger</span><span class="price">9</span></div>
      <p class="desc" style="width:222px;">Rice and beans, guacamole and pico<br><span class="note">Add a choice of: &nbsp;mushroom, spinach or peppers</span></p></div>
    <div class="item"><div class="item-head"><span class="item-name">Chefs Burger</span><span class="price">9</span></div>
      <p class="desc" style="width:200px;">Lettuce, tomato, pickle and onion</p></div>
    <div class="item"><div class="item-head"><span class="item-name">BBQ Pork Burger</span><span class="price">11</span></div>
      <p class="desc">Mojito pork cooked in BBQ topped with provolone and coleslaw</p></div>
    <div class="item"><div class="item-head"><span class="item-name">Louisiana Burger</span><span class="price">12</span></div>
      <p class="desc">Served with shrimp, chorizo, spinach and provolone</p></div>
    <p class="addon">+Enhance with an egg<span class="price">2</span></p>
  </section>

  <!-- Entree -->
  <h2 class="section-title" style="left:556px;top:220px;width:224px;">Entrée (Cena)</h2>
  <div class="section-rule" style="left:556px;top:254px;width:224px;"></div>
  <section class="column col-entree" style="left:558px;top:269px;">
    <div class="item"><div class="item-head"><span class="item-name">Barramundi</span><span class="price">19</span></div>
      <p class="desc">Texture of Asian sea bass with a mild and buttery taste of cod and served with a lemon sofrito cream sauce</p></div>
    <div class="item"><div class="item-head"><span class="item-name">Salmon</span><span class="price">17</span></div>
      <p class="desc">Grilled salmon on a bed of sautéed spinach, mushrooms &amp; sun-dried tomatoes, cream sauce</p></div>
    <div class="item"><div class="item-head"><span class="item-name">Chicken Marsala</span><span class="price">17</span></div>
      <p class="desc">Chicken breast cooked in mushroom brandy cream sauce</p></div>
    <div class="item"><div class="item-head"><span class="item-name">Chicken Piccatta</span><span class="price">17</span></div>
      <p class="desc">Chicken dredged in an egg batter, then sautéed with a lemon caper cream sauce</p></div>
    <div class="item"><div class="item-head"><span class="item-name">Artichoke Chicken</span><span class="price">17</span></div>
      <p class="desc" style="width:212px;">Chicken sautéed with sundried tomato, artichoke, spinach and red onion in a lemon twist cream sauce</p></div>
    <div class="item" style="margin-bottom:6px;"><div class="item-head"><span class="item-name">Voodoo Rogue</span><span class="price">17</span></div>
      <p class="desc">Chicken, shrimp, andouille, spinach cooked in a spiced Louisiana, merlot beer sauce</p></div>
    <p class="script">Entrée includes choice of:</p>
    <p class="desc" style="font-size:9px;width:212px;">Rice bowl or taco-style salad bowl: served with beans &amp; rice or salad</p>
    <p class="script-dark" style="text-align:right;margin-top:8px;padding-right:18px;">Extra plate charge <span class="price">5</span></p>
  </section>

  <!-- Entree salads -->
  <h2 class="section-title" style="left:68px;top:732px;width:228px;">Entrée Salads</h2>
  <div class="section-rule" style="left:70px;top:766px;width:224px;"></div>
  <section class="column col-appetizers" style="left:68px;top:781px;">
    <div class="item"><div class="item-head"><span class="item-name">Nacho Salad</span><span class="price">12</span></div>
      <p class="desc">Picadillo, chicken, mojito or add $4 for seafood on bed of artisan lettuce mix, pico, guac, sour cream</p>
      <div class="subline"><span>Without meat</span><span class="price">10</span></div></div>
  </section>

  <!-- Sandwiches -->
  <h2 class="section-title" style="left:70px;top:873px;width:228px;">Sandwiches</h2>
  <div class="section-rule" style="left:72px;top:907px;width:224px;"></div>
  <section class="column col-appetizers" style="left:70px;top:922px;">
    <div class="item"><div class="item-head"><span class="item-name">Milano Tripleta</span><span class="price">12</span></div>
      <p class="script-dark" style="width:140px;">The Puerto Rican famous meat lovers delight…</p>
      <p class="desc">Pernil (pork), grilled steak &amp; ham with melted Swiss cheese, shredded cabbage and TB's sauce &amp; pickles, served with bistro chips</p></div>
  </section>

  <!-- Stew -->
  <h2 class="section-title" style="left:314px;top:732px;width:224px;">Stew</h2>
  <div class="section-rule" style="left:314px;top:766px;width:224px;"></div>
  <section class="column col-wide" style="left:313px;top:781px;">
    <div class="item"><div class="item-head"><span class="item-name">Beef “Sancocho”</span><span class="price">12</span></div>
      <p class="desc">A rich Puerto Rican beef stew with plantains, yucca, potatoes, onion, and garlic made with a traditional “sofrito” peppers served with sazon rice</p></div>
    <div class="item"><div class="item-head"><span class="item-name">Paella</span><span class="price">20</span></div>
      <p class="desc" style="width:160px;">Shrimp, mussels, chorizo, pork mojito, spinach, onion, pepper and caper mix</p></div>
  </section>

  <!-- Kids menu -->
  <h2 class="section-title" style="left:314px;top:900px;width:224px;">Kids Menu</h2>
  <div class="section-rule" style="left:314px;top:934px;width:224px;"></div>
  <section class="column col-wide" style="left:313px;top:946px;">
    <div class="item"><div class="item-head"><span class="item-name">Chicken Bites</span><span class="price">6</span></div>
      <p class="desc">Served with bistro potatoes or fruit</p></div>
    <div class="item"><div class="item-head"><span class="item-name">Mini Cheeseburger</span><span class="price">6</span></div>
      <p class="desc">Cheddar, lettuce and tomato</p></div>
    <div class="item"><div class="item-head"><span class="item-name">Kids Quesadilla</span><span class="price">5</span></div>
      <p class="desc">Cheese or chicken with rice &amp; beans</p></div>
  </section>

  <!-- Drinks -->
  <h2 class="section-title" style="left:314px;top:1034px;width:224px;">Drinks</h2>
  <div class="section-rule" style="left:314px;top:1068px;width:224px;"></div>
  <section class="column col-wide" style="left:313px;top:1080px;">
    <div class="item"><div class="item-head"><span class="item-name">Mimosas</span><span class="price">8</span></div>
      <p class="desc">Classic orange, mango or passion fruit</p></div>
    <p class="script" style="width:210px;line-height:11px;">We pour only craft beers &amp; offer a great wine selection</p>
  </section>

  <div class="fine-print">
    <p class="script">Gluten-free requests can be accommodated</p>
    <p class="desc">*Consuming raw or under-cooked meats, poultry, seafood, shellfish or eggs may increase your risk of food-borne illness, especially if you have certain medical conditions.</p>
  </div>

  <div class="chef-feature" role="img" aria-label="Black and white photo of the chef in a dark chef coat holding a plated dish beside a pocket watch"></div>
  <div class="hours-card">
    <p class="big">Dinner</p>
    <p class="bigger">Menu</p>
    <p class="time">5PM</p>
    <p class="small">Until</p>
    <p class="small">Close</p>
  </div>
</main>
</body>
</html>
```